Animated Banner Design for a snacking company

We need a set of banner design to to fit the all the brindle promo spots designs. The banners should be animated and static. Our product has it colors identity that should be used with characters. it should match a movie that explains the product.

The product is subscription serivce that target individual with a healthy lifestyle.

Please visit nine.kovaleth.com and watch the movie on pix cast.

Target Market(s)

Males and Females Age from 18 to 38

Industry/Entity Type

Food Store

Other font styles liked:
• Lato

Colors
3176b5
f37122
5c5c5c

Requirements
Must have
• color scheme to match the video and color codes.
• animation

```html
<!DOCTYPE html>
<html lang="en">
<head>
<meta charset="utf-8">
<title>Brindle Promo Spots – Nuts Banner</title>
<link rel="stylesheet" href="https://fonts.googleapis.com/css2?family=Lato:wght@400;700;900&display=swap">
<style>
  :root {
    --frame-orange: #f37122;
    --brand-blue: #3176b5;
    --board-navy-dark: #172338;
    --board-navy-light: #2b3e5e;
    --text-white: #ffffff;
  }
  html, body {
    margin: 0;
    padding: 0;
    width: 1200px;
    height: 148px;
    overflow: hidden;
    background: #ffffff;
  }
  .banner {
    position: relative;
    box-sizing: border-box;
    width: 1200px;
    height: 148px;
    border: 5px solid var(--frame-orange);
    display: flex;
    background: var(--brand-blue);
  }
  .presenter-scene {
    width: 403px;
    height: 100%;
    flex: none;
    background: linear-gradient(120deg, var(--board-navy-light) 0%, var(--board-navy-dark) 70%);
  }
  .message {
    flex: 1;
    display: flex;
    flex-direction: column;
    justify-content: center;
    align-items: center;
    color: var(--text-white);
    font-family: "Lato", sans-serif;
    font-weight: 400;
    font-size: 29px;
    line-height: 44px;
    text-align: center;
    padding-bottom: 4px;
  }
  .message .highlight {
    font-weight: 900;
    text-transform: uppercase;
  }
  .message p {
    margin: 0;
  }
</style>
</head>
<body>
  <div class="banner">
    <div class="presenter-scene" role="img" aria-label="Illustrated presenter in a suit pointing at a chalkboard with a peanut diagram and a bar chart"></div>
    <div class="message">
      <p>Did you know, that <span class="highlight">eating a handful of nuts</span></p>
      <p>a day have huge health benefits?</p>
    </div>
  </div>
</body>
</html>
```